Business Card Design For A Renovation Contractor Company

We need a business card for a new company based in Singapore, our company name is "KT Planora". We are a renovation contractor that builds designs into reality. We build more of F&B restaurants, retail stores and commercial offices. We work very closely with designers. The final design should communicate to our client that we are a company that you can trust, that will plan and complete your project without giving you a headache. I like my client to remember my company as "KT". The beauty of SIMPLE is important.

Industry/Entity Type

Contractor

Requirements
Nice to have
• Black or Red base

```html
<!DOCTYPE html>
<html lang="en">
<head>
<meta charset="utf-8">
<title>KT Planora — Business Card</title>
<link href="https://fonts.googleapis.com/css2?family=Arimo:wght@400;700&display=swap" rel="stylesheet">
<style>
  :root {
    --paper: #ffffff;
    --card: #000000;
    --red: #ec1c24;
    --grey-line: #8a8a8a;
    --grey-faint: #3d3d3d;
    --grey-box: #d1d2d4;
    --ink: #000000;
    --white: #ffffff;
  }
  html, body {
    margin: 0;
    padding: 0;
    width: 1200px;
    height: 1000px;
    overflow: hidden;
    background: var(--paper);
  }
  .card {
    position: absolute;
    left: 73px;
    top: 173px;
    width: 1052px;
    height: 602px;
    background: var(--card);
    overflow: hidden;
    font-family: "Arimo", Arial, sans-serif;
  }
  .gear-decoration {
    position: absolute;
    left: 0;
    top: 42px;
    width: 245px;
    height: 520px;
    border-radius: 0 260px 260px 0;
    background: linear-gradient(90deg, #0a0a0a 0%, #1c1c1c 70%, #2a2a2a 100%);
    box-shadow: inset -2px 0 0 var(--grey-line);
  }
  .accent-dot {
    position: absolute;
    left: -42px;
    top: 264px;
    width: 84px;
    height: 84px;
    border-radius: 50%;
    background: var(--red);
  }
  .brand-mark {
    position: absolute;
    left: 229px;
    top: 190px;
    width: 230px;
    text-align: center;
    color: var(--white);
    font-weight: 700;
    font-size: 34px;
    line-height: 1;
  }
  .brand-faint {
    position: absolute;
    left: 528px;
    top: 262px;
    margin: 0;
    color: var(--grey-faint);
    font-weight: 400;
    font-size: 92px;
    line-height: 1;
    letter-spacing: -2px;
    white-space: nowrap;
  }
  .name-square {
    position: absolute;
    left: 580px;
    top: 320px;
    width: 170px;
    height: 68px;
    background: var(--grey-box);
  }
  .name-initials {
    position: absolute;
    left: 580px;
    top: 312px;
    width: 170px;
    margin: 0;
    color: var(--ink);
    font-weight: 700;
    font-size: 80px;
    line-height: 80px;
    text-align: center;
    letter-spacing: 4px;
  }
  .name-band {
    position: absolute;
    left: 730px;
    top: 305px;
    width: 322px;
    height: 47px;
    background: var(--red);
  }
  .company-name {
    position: absolute;
    left: 760px;
    top: 303px;
    margin: 0;
    color: var(--white);
    font-weight: 400;
    font-size: 46px;
    line-height: 50px;
    white-space: nowrap;
  }
  .stroke-line {
    position: absolute;
    left: 747px;
    top: 372px;
    width: 298px;
    height: 5px;
    background: linear-gradient(90deg, #6e6e6e, #b5b5b5 50%, #6e6e6e);
    border-radius: 2px;
  }
  .tagline {
    position: absolute;
    left: 686px;
    top: 388px;
    width: 351px;
    height: 24px;
    margin: 0;
    background: var(--white);
    color: var(--red);
    font-weight: 700;
    font-size: 20px;
    line-height: 24px;
    text-align: center;
    white-space: nowrap;
  }
</style>
</head>
<body>
  <div class="card">
    <div class="gear-decoration" role="img" aria-label="Large outlined gear decoration cut by the left edge"></div>
    <div class="accent-dot"></div>
    <div class="brand-mark">KT Planora</div>
    <p class="brand-faint" aria-hidden="true">KT Planora</p>
    <div class="name-square"></div>
    <div class="name-band"></div>
    <h1 class="company-name">Planora</h1>
    <p class="name-initials">KT</p>
    <div class="stroke-line"></div>
    <p class="tagline">turning plans into real spaces</p>
  </div>
</body>
</html>
```